Kestrel Property Management email template

Looking for an email template for communications sent to residents that reads well in most email formats including mobile devices. Similar to the attached email, not quite reclaimed wood but something warm with interesting texture

```html
<!DOCTYPE html>
<html lang="en">
<head>
<meta charset="utf-8">
<meta name="viewport" content="width=device-width, initial-scale=1">
<title>Kestrel Property Management — Urban Living</title>
<link rel="stylesheet" href="https://fonts.googleapis.com/css2?family=Archivo:wdth,wght@125,900&family=Jost:ital,wght@0,400;0,700;1,400&display=swap">
<style>
  :root {
    --page: #f6efe6;
    --espresso: #3a2820;
    --espresso-overlay: rgba(58, 38, 28, 0.88);
    --frame: #3a2820;
    --copper: #b8733f;
    --cream: #fffaf3;
    --sky-warm: #f3dcc0;
    --sky-amber: #d9a172;
    --tower-bronze: #8a5a3c;
    --tower-deep: #4a2f24;
    --street: #6e4a3a;
  }
  * { box-sizing: border-box; margin: 0; padding: 0; }
  html, body {
    width: 1043px; height: 1200px; overflow: hidden;
    background: var(--page);
  }
  .email {
    position: absolute; left: 40px; top: 261px;
    width: 963px; height: 677px; overflow: hidden;
    display: grid; grid-template-columns: 500px 1fr;
    font-family: "Jost", "Futura", sans-serif;
    color: var(--cream);
  }
  .email__aside-photo {
    grid-column: 1; grid-row: 1;
    background: linear-gradient(160deg, #8a6450 0%, var(--street) 50%, #4a2e24 100%);
  }
  .email__panel {
    grid-column: 1; grid-row: 1; position: relative;
    background:
      repeating-linear-gradient(92deg, rgba(255,235,210,0.035) 0 2px, transparent 2px 7px),
      repeating-linear-gradient(178deg, rgba(0,0,0,0.06) 0 1px, transparent 1px 5px),
      var(--espresso-overlay);
  }
  .email__hero-photo {
    grid-column: 2; grid-row: 1;
    background:
      linear-gradient(135deg, transparent 40%, var(--tower-bronze) 40%, #b98a62 62%, var(--tower-deep) 100%),
      linear-gradient(200deg, var(--cream) 0%, var(--sky-warm) 40%, var(--sky-amber) 100%);
  }
  .headline {
    position: absolute; left: 36px; top: 52px; line-height: 1;
  }
  .headline__bold {
    display: block;
    font-family: "Archivo", "Arial Black", sans-serif;
    font-weight: 900; font-stretch: 125%;
    font-variation-settings: "wdth" 125;
    font-size: 76px; letter-spacing: 3px;
  }
  .headline__light {
    display: block; margin-top: 4px;
    font-family: "Jost", sans-serif; font-weight: 400;
    font-size: 72px; letter-spacing: 27px;
  }
  .features {
    position: absolute; left: 40px; top: 232px; list-style: none;
  }
  .features__item {
    font-style: italic; font-size: 15px;
    height: 45px; line-height: 20px;
  }
  .features__item::before {
    content: "•"; font-style: normal; margin-right: 12px;
  }
  .intro {
    position: absolute; left: 38px; top: 562px; width: 446px;
    font-size: 13px; line-height: 15.5px;
  }
  .intro strong { font-weight: 700; }
  .callout {
    position: absolute; left: 0; top: 0; width: 963px; height: 677px;
  }
  .callout__frame { fill: var(--frame); }
  .callout__fill { fill: var(--cream); }
  .brand {
    position: absolute; left: 337px; top: 236px; width: 290px; height: 203px;
    display: flex; flex-direction: column; align-items: center; justify-content: center;
    color: var(--espresso);
  }
  .brand__mark {
    width: 44px; height: 44px; background: var(--copper); margin-bottom: 18px;
  }
  .brand__name {
    font-family: "Jost", sans-serif; font-weight: 400;
    font-size: 23px; line-height: 1.25; text-align: center; letter-spacing: 1px;
  }
  @media (max-width: 620px) {
    .email { position: static; width: 100%; height: auto; grid-template-columns: 1fr; }
  }
</style>
</head>
<body>
  <main class="email">
    <div class="email__aside-photo" role="img" aria-label="Photograph of city buildings and a street lamp behind the text panel"></div>
    <section class="email__panel">
      <h1 class="headline">
        <span class="headline__bold">URBAN</span>
        <span class="headline__light">LIVING</span>
      </h1>
      <ul class="features">
        <li class="features__item">Lorem Ipsum is simply dummy text</li>
        <li class="features__item">Lorem Ipsum is simply dummy text</li>
        <li class="features__item">Lorem Ipsum is simply dummy text</li>
        <li class="features__item">Lorem Ipsum is simply dummy text</li>
        <li class="features__item">Lorem Ipsum is simply dummy text</li>
        <li class="features__item">Lorem Ipsum is simply dummy text</li>
        <li class="features__item">Lorem Ipsum is simply dummy text</li>
      </ul>
      <p class="intro"><strong>LOREM IPSUM</strong> is simply dummy text of the printing and typesetting industry. Lorem Ipsum has been the industry's standard dummy text ever since the 1500s, when an unknown printer took a galley of type and scrambled it to make a type specimen book.</p>
    </section>
    <div class="email__hero-photo" role="img" aria-label="Photograph looking up at a glass office tower against a cloudy sky"></div>

    <svg class="callout" viewBox="0 0 963 677" aria-hidden="true">
      <path class="callout__frame" d="M329 228 H635 V457 H612 L705 505 L577 457 H329 Z"/>
      <path class="callout__fill" d="M337 236 H627 V449 H606 L684 492 L586 449 H337 Z"/>
    </svg>
    <div class="brand">
      <span class="brand__mark"></span>
      <span class="brand__name">Kestrel<br>Property Management</span>
    </div>
  </main>
</body>
</html>
```